We are in search of a new business card design for our business. We have a Mexican Grocery Store called Tamarindo Market, we would like to see that some have mexican design, but we are open to any type of designs.

Phone: to be announced
Fax: to be announced

Address is:
2465 Calloway Blvd
Dundalk, MD 21222

Industry/Entity Type

Business

```html
<!DOCTYPE html>
<html lang="en">
<head>
<meta charset="utf-8">
<title>Tamarindo Market – Business Card</title>
<link rel="stylesheet" href="https://fonts.googleapis.com/css2?family=Open+Sans:wght@400;600;700&display=swap">
<style>
  :root {
    --page-bg: #e9e6e4;
    --card-top-a: #fbf8f7;
    --card-top-b: #efe9e8;
    --brand-red: #a00000;
    --text-light: #ffffff;
  }
  html, body {
    margin: 0;
    width: 1200px;
    height: 900px;
    overflow: hidden;
    background: var(--page-bg);
    font-family: "Open Sans", Arial, sans-serif;
  }
  .card {
    position: absolute;
    left: 120px;
    top: 152px;
    width: 960px;
    height: 595px;
    box-shadow: 0 12px 36px rgba(0,0,0,0.18);
    overflow: hidden;
  }
  .card-top {
    position: absolute;
    inset: 0 0 auto 0;
    height: 322px;
    background: linear-gradient(180deg, var(--card-top-a), var(--card-top-b));
    display: flex;
    align-items: center;
    justify-content: center;
  }
  .brand-name {
    display: flex;
    align-items: center;
    gap: 16px;
    color: var(--brand-red);
    font-weight: 700;
    font-size: 52px;
    letter-spacing: 0.5px;
  }
  .brand-dot {
    width: 34px;
    height: 34px;
    border-radius: 50%;
    background: var(--brand-red);
  }
  .card-bottom {
    position: absolute;
    inset: 322px 0 0 0;
    background: var(--brand-red);
    color: var(--text-light);
  }
  .person {
    position: absolute;
    left: 48px;
    top: 80px;
  }
  .person-name {
    font-size: 31px;
    font-weight: 600;
    line-height: 1.2;
  }
  .person-role {
    font-size: 24px;
    line-height: 1.3;
  }
  .address {
    position: absolute;
    left: 330px;
    top: 68px;
    font-size: 24px;
    line-height: 34px;
  }
  .contacts {
    position: absolute;
    left: 588px;
    top: 68px;
    margin: 0;
    padding: 0;
    list-style: none;
    font-size: 24px;
    line-height: 34px;
  }
  .contacts li {
    display: flex;
    align-items: center;
    gap: 14px;
  }
  .contacts svg {
    width: 20px;
    height: 20px;
    fill: var(--text-light);
    flex: none;
  }
</style>
</head>
<body>
  <div class="card">
    <div class="card-top">
      <div class="brand-name"><span class="brand-dot"></span>Tamarindo Market</div>
    </div>
    <div class="card-bottom">
      <div class="person">
        <div class="person-name">Marco Alvarez</div>
        <div class="person-role">Managing Director</div>
      </div>
      <div class="address">
        2465 Calloway Blvd,<br>
        Dundalk, MD<br>
        21222.
      </div>
      <ul class="contacts">
        <li>
          <svg viewBox="0 0 24 24" aria-hidden="true"><path d="M6.6 10.8a15.1 15.1 0 0 0 6.6 6.6l2.2-2.2a1 1 0 0 1 1-.25 11.4 11.4 0 0 0 3.6.57 1 1 0 0 1 1 1V20a1 1 0 0 1-1 1A17 17 0 0 1 3 4a1 1 0 0 1 1-1h3.5a1 1 0 0 1 1 1c0 1.25.2 2.45.57 3.57a1 1 0 0 1-.25 1z"/></svg>
          410-555 0187
        </li>
        <li>
          <svg viewBox="0 0 24 24" aria-hidden="true"><path d="M3 6h18v12H3V6zm2 2v.3l7 4.4 7-4.4V8H5z"/></svg>
          hola@tamarindomkt.com
        </li>
        <li>
          <svg viewBox="0 0 24 24" aria-hidden="true"><circle cx="12" cy="12" r="9"/><path d="M8 9l3 1 1 3-2 2 1 3" stroke="#a00000" stroke-width="1.6" fill="none"/></svg>
          www.tamarindomkt.com
        </li>
      </ul>
    </div>
  </div>
</body>
</html>
```